Homepage Real Estate Agency

I need a web design for a real estate agency in Luxembourg. A short draft for the front page can be found in the project details. (Page 1+2) The main colors of the site should be blue as shown in the project details. (Page 3)
The main target for this site is to promote real estates and a small presentation of the company.

Industry/Entity Type

Real Estate

Requirements
Must have
• On the front page estates are shown in a short preview in small boxes, on the right side is a search. The search is hidden except for the front page. The header has 4 buttons and the logo of the company.

```html
<!DOCTYPE html>
<html lang="fr">
<head>
<meta charset="utf-8">
<title>Maisonvale – Immobilier</title>
<link href="https://fonts.googleapis.com/css2?family=Oswald:wght@300;400&family=Noto+Sans:wght@400;700&display=swap" rel="stylesheet">
<style>
:root{
  --blue-deep:#1c5aab;
  --blue-soft:#8daedb;
  --red:#c8000a;
  --red-dark:#98000c;
  --orange:#ea8a1c;
  --orange-light:#f0b02c;
  --violet:#8a7ed6;
  --violet-dark:#5a4ea6;
  --grey-panel:#e2e2e2;
  --grey-text:#666;
  --white:#fff;
  --heading:"Oswald",sans-serif;
  --body:"Noto Sans",sans-serif;
}
*{box-sizing:border-box;margin:0;padding:0}
html,body{width:1059px;height:1200px;overflow:hidden}
body{position:relative;background:#fff;font-family:var(--body);color:var(--grey-text)}
.abs{position:absolute}

.header{left:0;top:0;width:1059px;height:144px;background:linear-gradient(#dcdcdc,#fff 40%,#fff)}
.brand{left:106px;top:0;width:163px;height:141px;background:linear-gradient(#fff,#e6e6e6);border-radius:0 0 26px 10px;box-shadow:0 2px 4px rgba(0,0,0,.2);display:flex;align-items:center;justify-content:center;gap:6px}
.brand-dot{width:14px;height:14px;border-radius:50%;background:var(--blue-deep)}
.brand-name{font-family:var(--body);font-weight:700;font-size:18px;color:var(--red)}
.account{right:106px;top:18px;font-size:11px;color:var(--red)}
.account span{color:#999;margin:0 4px}
.nav{top:109px;height:32px;display:flex;align-items:center;justify-content:center;font-family:var(--heading);font-weight:400;font-size:17px;color:var(--white);border-radius:3px;text-transform:uppercase;letter-spacing:0;white-space:nowrap;background:linear-gradient(var(--red),var(--red-dark));border:1px solid #fff;box-shadow:0 0 0 1px #a00}
.nav.current{background:linear-gradient(#3fa437,#1f6b1c);color:#111;box-shadow:0 0 0 1px #1f6b1c}

.stage{left:0;top:144px;width:1059px;height:897px;background:linear-gradient(var(--blue-deep) 0%,#2764b4 45%,var(--blue-soft) 100%)}
.slider{left:119px;top:154px;width:821px;height:271px;background:#fff}
.slide{left:126px;top:160px;width:807px;height:259px;background:linear-gradient(160deg,#c8905a 0%,#8a4a2a 40%,#2a1c12 85%)}
.arrow{top:254px;width:50px;height:78px}

.section-title{font-family:var(--heading);font-weight:300;font-size:21px;color:var(--white)}
.rule{left:118px;top:494px;width:559px;border-top:1px dotted #9ebbe6}

.offer{top:501px;height:284px;color:var(--white);padding:0 13px}
.offer.orange{background:linear-gradient(var(--orange),var(--orange-light))}
.offer.red{background:linear-gradient(var(--red),var(--red-dark))}
.offer.violet{background:linear-gradient(var(--violet),var(--violet-dark))}
.offer .frame{position:absolute;left:13px;top:9px;width:166px;height:147px;border:1px solid #fff;padding:5px;background:rgba(255,255,255,.9)}
.offer .photo{width:100%;height:100%}
.offer .name{position:absolute;top:162px;font-size:13px}
.offer .price{position:absolute;top:180px;font-size:13px}
.offer .price b{font-weight:400;color:#c37a14}
.offer.red .price b{color:#8a000a}
.offer.violet .price b{color:#c8c0f0}
.offer .blurb{position:absolute;top:204px;font-size:10.5px;line-height:14px}
.details{position:absolute;top:257px;width:86px;height:20px;border-radius:10px;background:linear-gradient(#d0000c,#8c000a);border:1px solid #fff;font-size:11px;color:#fff;padding-left:23px;line-height:18px}
.details::after{content:"";position:absolute;right:5px;top:5px;width:8px;height:8px;border-radius:50%;background:#fff}

.search{left:699px;top:455px;width:254px;height:330px;background:var(--grey-panel);border:4px solid #fff;padding:0 10px}
.search h2{font-family:var(--heading);font-weight:300;font-size:20px;color:#666;margin-top:6px;padding-bottom:5px;border-bottom:1px solid #ccc}
.field-label{position:absolute;font-size:11px;color:#555}
.input{position:absolute;height:18px;background:#fff;border:1px solid #bbb}
.select{position:absolute;height:19px;background:#fff;border:1px solid #bbb;font-size:10px;padding-left:8px;line-height:17px;color:#555}
.select::after{content:"";position:absolute;right:1px;top:1px;width:15px;height:15px;background:linear-gradient(#5cb4ee,#2a80c8)}
.go{position:absolute;left:112px;top:267px;width:123px;height:28px;border-radius:14px;background:linear-gradient(#d6000c,#92000a);color:#fff;font-size:12px;line-height:28px;padding-left:8px}
.go::after{content:"›";position:absolute;right:4px;top:5px;width:18px;height:18px;border-radius:50%;background:#bbb;color:#fff;line-height:16px;text-align:center;font-size:14px}
.hint{position:absolute;left:10px;top:299px;font-size:9px;line-height:12px;color:#666}

.category{top:815px;height:216px;color:#fff}
.category.orange{background:linear-gradient(var(--orange),var(--orange-light))}
.category.red{background:linear-gradient(var(--red),var(--red-dark))}
.category.violet{background:linear-gradient(var(--violet),var(--violet-dark))}
.category h3{font-family:var(--heading);font-weight:300;font-size:21px;position:absolute;left:10px;top:6px}
.category .frame{position:absolute;top:60px;height:123px;border:1px solid #fff;padding:5px;background:rgba(255,255,255,.85)}
.category .photo{width:100%;height:100%}

.footer{left:0;top:1041px;width:1059px;height:159px;background:linear-gradient(#e9e9e9,#fff 60%);border-top:7px solid #a8a8a8}
.footer-title{font-family:var(--heading);font-weight:300;font-size:20px;color:#777}
.locality{top:1088px;width:110px}
.locality h4{font-weight:400;font-size:12.5px;color:var(--red);margin-bottom:5px}
.locality li,.links li{list-style:none;font-size:11px;line-height:14.2px;color:#777}
.links{left:691px;top:1082px}
.divider{left:674px;top:1058px;height:128px;border-left:1px solid #ccc}
.social{top:1087px;width:26px;height:26px;border-radius:5px}
.copyright{right:106px;top:1186px;font-size:10px;line-height:12px;color:var(--red)}
</style>
</head>
<body>

<header class="abs header"></header>
<div class="abs brand"><span class="brand-dot"></span><span class="brand-name">Maisonvale</span></div>
<div class="abs account">Login<span>|</span>Signup</div>
<a class="abs nav current" style="left:445px;width:76px">Home</a>
<a class="abs nav" style="left:529px;width:86px">A Vendre</a>
<a class="abs nav" style="left:626px;width:112px">Construction</a>
<a class="abs nav" style="left:747px;width:83px">Location</a>
<a class="abs nav" style="left:844px;width:109px">Cherchons</a>

<main class="abs stage"></main>

<div class="abs slider"></div>
<div class="abs slide" role="img" aria-label="Grande villa avec balcons au coucher du soleil"></div>
<svg class="abs arrow" style="left:119px" viewBox="0 0 50 78"><circle cx="10" cy="39" r="38" fill="#2052a8" stroke="#1a3f88" stroke-width="1"/><path d="M24 29 L16 39 L24 49" fill="none" stroke="#d80010" stroke-width="5"/></svg>
<svg class="abs arrow" style="left:891px" viewBox="0 0 50 78"><circle cx="40" cy="39" r="38" fill="#2052a8" stroke="#1a3f88" stroke-width="1"/><path d="M26 29 L34 39 L26 49" fill="none" stroke="#d80010" stroke-width="5"/></svg>

<h2 class="abs section-title" style="left:118px;top:463px">Featured Offers</h2>
<div class="abs rule"></div>

<article class="abs offer orange" style="left:106px;width:190px">
  <div class="frame"><div class="photo" role="img" aria-label="Maison bleue avec clôture blanche" style="background:linear-gradient(#d8e4ee,#4a4a6a 50%,#5a7a3a)"></div></div>
  <p class="name">sample text</p>
  <p class="price">Price: <b>0000000</b></p>
  <p class="blurb">sample text sample text<br>sample text sample text<br>sample text sample text</p>
  <a class="details" style="left:13px">Details</a>
</article>
<article class="abs offer red" style="left:301px;width:191px">
  <div class="frame"><div class="photo" role="img" aria-label="Maison jaune avec jardin" style="background:linear-gradient(#3a6ab0,#c8a048 50%,#2a4a1a)"></div></div>
  <p class="name">sample text</p>
  <p class="price">Price: <b>0000000</b></p>
  <p class="blurb">sample text sample text<br>sample text sample text<br>sample text sample text</p>
  <a class="details" style="left:13px">Details</a>
</article>
<article class="abs offer violet" style="left:499px;width:188px">
  <div class="frame"><div class="photo" role="img" aria-label="Maison de campagne avec fleurs" style="background:linear-gradient(#e8eef4,#c8a880 45%,#4a7a2a)"></div></div>
  <p class="name">sample text</p>
  <p class="price">Price: <b>0000000</b></p>
  <p class="blurb">sample text sample text<br>sample text sample text<br>sample text sample text</p>
  <a class="details" style="left:17px">Details</a>
</article>

<aside class="abs search">
  <h2>Find Your Property</h2>
  <span class="field-label" style="left:10px;top:48px">City:</span>
  <span class="field-label" style="left:138px;top:48px">State:</span>
  <div class="input" style="left:10px;top:66px;width:100px"></div>
  <div class="input" style="left:138px;top:66px;width:100px"></div>
  <span class="field-label" style="left:13px;top:93px">Zip:</span>
  <span class="field-label" style="left:138px;top:93px">Country:</span>
  <div class="input" style="left:10px;top:111px;width:103px"></div>
  <div class="input" style="left:138px;top:111px;width:100px"></div>
  <span class="field-label" style="left:13px;top:137px">Price Range:</span>
  <div class="select" style="left:13px;top:155px;width:98px">Max</div>
  <span class="field-label" style="left:116px;top:158px">To:</span>
  <div class="select" style="left:138px;top:155px;width:100px">Min</div>
  <span class="field-label" style="left:13px;top:182px">Bedroom:</span>
  <div class="select" style="left:13px;top:200px;width:225px"></div>
  <span class="field-label" style="left:13px;top:225px">Bathroom:</span>
  <div class="select" style="left:13px;top:243px;width:225px"></div>
  <a class="go">Search Property</a>
  <p class="hint">Know exactly what you want?<br>Advanced search</p>
</aside>

<section class="abs category orange" style="left:106px;width:167px"><h3>Owners</h3>
  <div class="frame" style="left:16px;width:134px"><div class="photo" role="img" aria-label="Maison bleue avec clôture" style="background:linear-gradient(#d8e4ee,#4a4a6a 50%,#5a7a3a)"></div></div></section>
<section class="abs category red" style="left:281px;width:163px"><h3>Agents</h3>
  <div class="frame" style="left:13px;width:138px"><div class="photo" role="img" aria-label="Maison blanche" style="background:linear-gradient(#dce6f0,#e8e4dc 55%,#4a6a2a)"></div></div></section>
<section class="abs category violet" style="left:452px;width:169px"><h3>Rentals</h3>
  <div class="frame" style="left:12px;width:140px"><div class="photo" role="img" aria-label="Maison en briques" style="background:linear-gradient(#e8eef4,#8a4a3a 50%,#5a7a3a)"></div></div></section>
<section class="abs category orange" style="left:627px;width:157px"><h3>Sellers</h3>
  <div class="frame" style="left:8px;width:140px"><div class="photo" role="img" aria-label="Rue de maisons résidentielles" style="background:linear-gradient(#6a9ad8,#d8c8a0 50%,#4a6a2a)"></div></div></section>
<section class="abs category red" style="left:789px;width:164px"><h3>Buyers</h3>
  <div class="frame" style="left:14px;width:138px"><div class="photo" role="img" aria-label="Grande maison familiale" style="background:linear-gradient(#8ab0e0,#b8a488 50%,#5a7a3a)"></div></div></section>

<footer class="abs footer"></footer>
<h2 class="abs footer-title" style="left:108px;top:1051px">Browse Propery by Locality</h2>
<div class="abs locality" style="left:108px"><h4>Country Name</h4><ul><li>sample link</li><li>sample link</li><li>sample link</li><li>sample link</li><li>sample link</li></ul></div>
<div class="abs locality" style="left:229px"><h4>Country Name</h4><ul><li>sample link</li><li>sample link</li><li>sample link</li><li>sample link</li><li>sample link</li></ul></div>
<div class="abs locality" style="left:345px"><h4>Country Name</h4><ul><li>sample link</li><li>sample link</li><li>sample link</li><li>sample link</li><li>sample link</li></ul></div>
<div class="abs locality" style="left:456px"><h4>Country Name</h4><ul><li>sample link</li><li>sample link</li><li>sample link</li><li>sample link</li><li>sample link</li></ul></div>
<div class="abs locality" style="left:574px"><h4>Country Name</h4><ul><li>sample link</li><li>sample link</li><li>sample link</li><li>sample link</li><li>sample link</li></ul></div>

<div class="abs divider"></div>
<h2 class="abs footer-title" style="left:691px;top:1051px">Links</h2>
<ul class="abs links"><li>Home</li><li>About Us</li><li>A Vendre</li><li>Construction</li><li>Location</li><li>Cherchons</li><li>Contact Us</li></ul>

<h2 class="abs footer-title" style="left:838px;top:1051px">Follow Us</h2>
<span class="abs social" style="left:836px;background:#3b5a9a" role="img" aria-label="Réseau social 1"></span>
<span class="abs social" style="left:874px;background:#3aa8d8" role="img" aria-label="Réseau social 2"></span>
<span class="abs social" style="left:911px;background:#1a6aa0" role="img" aria-label="Réseau social 3"></span>

<p class="abs copyright">© copyright 2012 by Real estate all rights reserved.</p>

</body>
</html>
```